Store Fixture business needs a buisness card design

We are looking for a business card design for a store fixture company. "KL Shelf Outfitters" we help small businesses with their start up by providing fixtures required to display their products.
It should have a simple yet innovative design in the front, and a refined look to our company.
We would like our logo, to have one of our products "display cases, clothing rack, mannequins" integrated in the design. And the rest of it just a clean look, which gives our address, store hours, and contact number, etc.
The color scheme as seen in the samples can be changed as long as the goal is achieved.
Industry/Entity Type
Business
Contact Information for Business Card
KL Shelf Outfitters
4362 Marlow Ave.
San Antonio,TX 78299
www.klshelfoutfitters.example
klpo@klshelfoutfitter.example
(210) 555-0188
M-F: 9-6pm
Sat: 10-3pm

```html
<!DOCTYPE html>
<html lang="en">
<head>
<meta charset="utf-8">
<title>KL Shelf Outfitters – Business Card</title>
<link href="https://fonts.googleapis.com/css2?family=Roboto:wght@400;500;700&display=swap" rel="stylesheet">
<style>
  :root {
    --page-bg: #e7e7e7;
    --card-white: #ffffff;
    --gold: #e2a531;
    --gold-deep: #b7791c;
    --brown: #5a3a16;
    --brown-dark: #3b240c;
    --ink: #4a4a4a;
    --ink-soft: #6b6b6b;
    --frame: #c9c9c9;
    --stripe: #bdbdbd;
  }
  * { box-sizing: border-box; margin: 0; padding: 0; }
  html, body { width: 1200px; height: 950px; overflow: hidden; }
  body {
    background: var(--page-bg);
    font-family: "Roboto", Arial, sans-serif;
    display: flex;
    flex-direction: column;
    align-items: center;
    justify-content: center;
    gap: 34px;
  }
  .card {
    position: relative;
    width: 760px;
    height: 434px;
    background: var(--card-white);
    box-shadow: 0 6px 18px rgba(0,0,0,0.18);
    overflow: hidden;
  }

  /* Front */
  .front-brand {
    position: absolute;
    top: 46px;
    left: 0;
    right: 0;
    display: flex;
    justify-content: center;
    align-items: center;
    gap: 14px;
  }
  .brand-square {
    width: 46px;
    height: 46px;
    background: var(--gold);
  }
  .brand-name {
    font-weight: 700;
    font-size: 34px;
    color: var(--ink);
    letter-spacing: 0.5px;
  }
  .front-hours {
    position: absolute;
    top: 114px;
    left: 0;
    right: 0;
    text-align: center;
    font-size: 17px;
    color: var(--ink-soft);
  }
  .front-hours .divider { margin: 0 10px; }
  .product-row {
    position: absolute;
    top: 170px;
    left: 0;
    right: 0;
    display: flex;
    justify-content: center;
    gap: 34px;
  }
  .product-tile {
    width: 190px;
    height: 190px;
    border: 2px solid var(--frame);
    border-radius: 18px;
    padding: 14px;
    background: var(--card-white);
  }
  .product-fill {
    width: 100%;
    height: 100%;
    border-radius: 10px;
  }
  .fill-rack { background: linear-gradient(160deg, #f4f4f4, #d9d9d9); }
  .fill-case { background: linear-gradient(180deg, #f1eded 0%, #e8dede 55%, #b8322c 56%, #8f2420 100%); }
  .fill-mannequin { background: linear-gradient(160deg, #5c5c5c, #2e2e2e); }

  /* Back */
  .back-art { position: absolute; inset: 0; }
  .back-brand {
    position: absolute;
    top: 150px;
    left: 70px;
    display: flex;
    align-items: center;
    gap: 16px;
  }
  .brand-circle {
    width: 70px;
    height: 70px;
    border-radius: 50%;
    background: var(--gold-deep);
  }
  .back-brand .brand-name {
    font-size: 24px;
    font-weight: 500;
    color: var(--gold-deep);
  }
  .contact-block {
    position: absolute;
    top: 70px;
    right: 44px;
    text-align: right;
    color: #ffffff;
  }
  .person-name { font-size: 22px; font-weight: 700; }
  .person-title { font-size: 16px; margin-bottom: 16px; }
  .contact-line {
    display: flex;
    justify-content: flex-end;
    align-items: center;
    gap: 10px;
    font-size: 16px;
    line-height: 26px;
  }
  .contact-line .icon { width: 16px; height: 16px; flex: none; }
  .contact-line .icon-space { width: 16px; flex: none; }
</style>
</head>
<body>

  <section class="card card-front">
    <div class="front-brand">
      <span class="brand-square"></span>
      <span class="brand-name">KL Shelf Outfitters</span>
    </div>
    <p class="front-hours">Mon-Fri: 9-6pm<span class="divider">|</span>Sat: 10-3pm</p>
    <div class="product-row">
      <div class="product-tile"><div class="product-fill fill-rack" role="img" aria-label="Line drawing of a rolling clothing rack"></div></div>
      <div class="product-tile"><div class="product-fill fill-case" role="img" aria-label="Photo of a glass display case with red base"></div></div>
      <div class="product-tile"><div class="product-fill fill-mannequin" role="img" aria-label="Photo of a silver display mannequin on a dark background"></div></div>
    </div>
  </section>

  <section class="card card-back">
    <svg class="back-art" viewBox="0 0 760 434" preserveAspectRatio="none" aria-hidden="true">
      <defs>
        <radialGradient id="goldGlow" cx="0.72" cy="0.35" r="0.75">
          <stop offset="0" stop-color="#f0ae3a"/>
          <stop offset="0.45" stop-color="#b8761f"/>
          <stop offset="1" stop-color="#3b240c"/>
        </radialGradient>
      </defs>
      <path d="M300 0 C 440 0, 395 150, 325 255 C 265 340, 180 330, 0 335 L 0 434 L 760 434 L 760 0 Z" fill="#bdbdbd"/>
      <path d="M318 0 C 460 0, 418 152, 348 262 C 290 352, 200 350, 0 354 L 0 434 L 760 434 L 760 0 Z" fill="#ffffff"/>
      <path d="M332 0 C 478 0, 436 156, 366 268 C 306 362, 214 366, 0 370 L 0 434 L 760 434 L 760 0 Z" fill="url(#goldGlow)"/>
    </svg>

    <div class="back-brand">
      <span class="brand-circle"></span>
      <span class="brand-name">KL Shelf Outfitters</span>
    </div>

    <div class="contact-block">
      <p class="person-name">Mara Ellison</p>
      <p class="person-title">President</p>
      <p class="contact-line">4362 Marlow Ave.<span class="icon-space"></span></p>
      <p class="contact-line">San Antonio,TX 78299
        <svg class="icon" viewBox="0 0 16 16"><path d="M4 1 L6.5 4 L5 6 C6 8.5 7.5 10 10 11 L12 9.5 L15 12 L13 15 C7 14 2 9 1 3 Z" fill="#fff"/></svg>
      </p>
      <p class="contact-line">(210) 555-0188<span class="icon-space"></span></p>
      <p class="contact-line">klpo@klshelfoutfitter.example
        <svg class="icon" viewBox="0 0 16 16"><rect x="1" y="3" width="14" height="10" fill="#fff"/><path d="M1 3 L8 9 L15 3" stroke="#7a4c18" stroke-width="1.4" fill="none"/></svg>
      </p>
      <p class="contact-line">www.klshelfoutfitters.example
        <svg class="icon" viewBox="0 0 16 16"><circle cx="8" cy="8" r="7" fill="#fff"/><path d="M1 8 H15 M8 1 C4 5 4 11 8 15 M8 1 C12 5 12 11 8 15" stroke="#7a4c18" stroke-width="1.1" fill="none"/></svg>
      </p>
    </div>
  </section>

</body>
</html>
```